Business card design for Tolbrin Waste

I would like double-sided business cards for myself and my partner that includes our logo and the existing colour scheme. We provide waste and environmental services to customers in the motor-vehicle and engineering industries.

```html
<!DOCTYPE html>
<html lang="en">
<head>
<meta charset="utf-8">
<title>Tolbrin Waste business card</title>
<link href="https://fonts.googleapis.com/css2?family=Arimo:wght@400;700&display=swap" rel="stylesheet">
<style>
  :root {
    --stage: #ecebe8;
    --green-light: #9ccf74;
    --green-mid: #6db543;
    --green-deep: #3d8a27;
    --green-text: #5aa532;
    --green-soft: #8cc05a;
    --ink: #222222;
    --muted: #666666;
    --white: #ffffff;
    --rule: #c9c9c9;
  }
  * { box-sizing: border-box; margin: 0; padding: 0; }
  html, body { width: 1200px; height: 913px; overflow: hidden; }
  body {
    background: var(--stage);
    font-family: "Arimo", Arial, sans-serif;
    display: flex;
    flex-direction: column;
    align-items: center;
    justify-content: center;
    gap: 56px;
  }
  .card {
    width: 640px;
    height: 366px;
    border-radius: 4px;
    box-shadow: 0 10px 28px rgba(0,0,0,0.18);
    position: relative;
    overflow: hidden;
  }
  /* front */
  .card-front {
    background: linear-gradient(135deg, var(--green-light) 0%, var(--green-mid) 45%, var(--green-deep) 100%);
    display: flex;
    align-items: center;
    justify-content: center;
    gap: 22px;
  }
  .brand-dot {
    width: 74px; height: 74px;
    border-radius: 50%;
    border: 5px solid var(--white);
  }
  .brand-name {
    color: var(--white);
    font-weight: 700;
    font-size: 58px;
    letter-spacing: 1px;
    text-transform: uppercase;
  }
  /* back */
  .card-back {
    background: var(--white);
    display: grid;
    grid-template-columns: 1fr 1px 1fr;
  }
  .back-left { padding: 52px 20px 40px 44px; }
  .back-brand {
    display: flex; align-items: center; gap: 12px;
    margin-bottom: 28px;
  }
  .back-brand .brand-dot {
    width: 40px; height: 40px; border: 3px solid var(--green-mid);
  }
  .back-brand .brand-name {
    color: var(--green-text);
    font-size: 32px;
    letter-spacing: 0.5px;
  }
  .tagline {
    color: var(--green-text);
    font-weight: 700;
    font-size: 19px;
    margin-bottom: 8px;
  }
  .services { list-style: none; color: var(--ink); font-size: 16px; line-height: 1.38; }
  .services li::before { content: "*"; }
  .divider {
    background: linear-gradient(to bottom, transparent, var(--rule) 20%, var(--rule) 80%, transparent);
  }
  .back-right { padding: 60px 36px 40px 34px; }
  .person-name { color: var(--green-soft); font-size: 24px; }
  .job-title { color: var(--muted); font-size: 15px; margin-top: 4px; }
  .contacts { list-style: none; margin-top: 52px; }
  .contacts li {
    display: flex; align-items: center; gap: 10px;
    font-size: 16px; color: var(--ink);
    margin-bottom: 10px;
  }
  .contact-icon {
    width: 20px; height: 20px; flex: none;
    border-radius: 50%;
    background: var(--green-mid);
    display: flex; align-items: center; justify-content: center;
  }
</style>
</head>
<body>
  <section class="card card-front" aria-label="Card front">
    <span class="brand-dot"></span>
    <span class="brand-name">Tolbrin Waste</span>
  </section>

  <section class="card card-back" aria-label="Card back">
    <div class="back-left">
      <div class="back-brand">
        <span class="brand-dot"></span>
        <span class="brand-name">Tolbrin Waste</span>
      </div>
      <p class="tagline">Your one stop shop for waste</p>
      <ul class="services">
        <li>Reuse, recycling and disposal</li>
        <li>Controlled and hazardous wastes</li>
        <li>Waste audits and reporting</li>
        <li>Consultancy and advice</li>
      </ul>
    </div>
    <div class="divider"></div>
    <div class="back-right">
      <p class="person-name">Your Name</p>
      <p class="job-title">Job Title</p>
      <ul class="contacts">
        <li>
          <span class="contact-icon">
            <svg width="11" height="11" viewBox="0 0 24 24"><path fill="#fff" d="M6.6 10.8a15 15 0 0 0 6.6 6.6l2.2-2.2a1 1 0 0 1 1-.25 11.4 11.4 0 0 0 3.6.57 1 1 0 0 1 1 1V20a1 1 0 0 1-1 1A17 17 0 0 1 3 4a1 1 0 0 1 1-1h3.5a1 1 0 0 1 1 1c0 1.25.2 2.45.57 3.57a1 1 0 0 1-.25 1z"/></svg>
          </span>
          +20 100 4821 307
        </li>
        <li>
          <span class="contact-icon">
            <svg width="11" height="11" viewBox="0 0 24 24"><rect x="2" y="5" width="20" height="14" rx="2" fill="#fff"/><path d="M3 6l9 7 9-7" stroke="#6db543" stroke-width="2" fill="none"/></svg>
          </span>
          name@tolbrinwaste.com
        </li>
        <li>
          <span class="contact-icon">
            <svg width="11" height="11" viewBox="0 0 24 24"><circle cx="12" cy="12" r="9" stroke="#fff" stroke-width="2.4" fill="none"/><path d="M3 12h18M12 3c3 3 3 15 0 18M12 3c-3 3-3 15 0 18" stroke="#fff" stroke-width="2" fill="none"/></svg>
          </span>
          www.tolbrinwaste.com
        </li>
      </ul>
    </div>
  </section>
</body>
</html>
```